I have a haircare line called Veltrix Professional. I’m branching out to create a line of Humanistic haircare products for pets. I want it to look similar to my Veltrix haircare Line. By adding some type of creative way of incorporating the word Pet. I am also attaching an image of Dorian Haskel Pet. I do not want it to look too similar to this as our looks are both clean and contemporary. I also am entertaining changing the bottles from cylinder to boston round. I will attach my new haircare packaging aswell. Please note that the boston round bottles are the round bottles attached not the tall square ones. They can be made black or white or natural plastic. Please use this shape to come up with a thought. I do what to keep my black and white motif. The word Pet can be maybe made bold to stand out but think fun and maybe some type of symbol that creates a pet theme. I also do the conditioner in the reverse color of the shampoo which makes the shampoo/conditioner package. Please keep this in mind aswell.

Target Market(s)

Boutique pet stores, Furlane

Industry/Entity Type

Hair Care Product

Logo Text

Veltrix Pro Pet

Colors

Designer to choose colors to be used in the design.

Requirements
Must have
• Shampoo/conditioner designs
Nice to have
• Want to keep the black and white motif but open to new ideas aswell
Should not have
• Should look expensive and modern

```html
<!DOCTYPE html>
<html lang="en">
<head>
<meta charset="UTF-8">
<title>Veltrix Professional – Pet Shampoo Label</title>
<link rel="stylesheet" href="https://fonts.googleapis.com/css2?family=Montserrat:wght@300;400;600;700&display=swap">
<style>
  :root {
    --page: #ffffff;
    --label: #333233;
    --ink: #ffffff;
    --rule: #d9d9d9;
    --icon-tone: #4a494a;
  }
  * { margin: 0; padding: 0; box-sizing: border-box; }
  html, body {
    width: 1200px;
    height: 2215px;
    overflow: hidden;
    background: var(--page);
    font-family: "Montserrat", sans-serif;
    color: var(--ink);
  }
  .label {
    position: absolute;
    left: 343px;
    top: 620px;
    width: 434px;
    height: 1180px;
    background: var(--label);
  }
  .label-frame {
    position: absolute;
    inset: 10px;
    border: 1.5px solid var(--rule);
  }
  .brand {
    position: absolute;
    top: 70px;
    left: 0;
    right: 0;
    text-align: center;
  }
  .brand-mark {
    display: block;
    width: 56px;
    height: 56px;
    margin: 0 auto 44px;
    border: 2px solid var(--ink);
    border-radius: 50%;
  }
  .brand-name {
    font-weight: 300;
    font-size: 40px;
    letter-spacing: 1px;
    line-height: 1;
  }
  .brand-tagline {
    margin-top: 6px;
    font-weight: 300;
    font-size: 13px;
    letter-spacing: 5px;
  }
  .product-name {
    position: absolute;
    top: 440px;
    left: 0;
    right: 0;
    text-align: center;
    font-weight: 300;
    font-size: 46px;
    line-height: 1.4;
    letter-spacing: 2px;
  }
  .pet-icon {
    position: absolute;
    top: 586px;
    left: 110px;
    width: 212px;
    height: 150px;
    background: var(--icon-tone);
    border-radius: 12px;
  }
  .claim {
    position: absolute;
    top: 840px;
    left: 0;
    right: 0;
    text-align: center;
  }
  .claim-title {
    font-weight: 700;
    font-size: 21px;
    letter-spacing: 1px;
  }
  .claim-note {
    margin-top: 4px;
    font-weight: 400;
    font-size: 20px;
    letter-spacing: 0.5px;
  }
  .net-weight {
    position: absolute;
    top: 938px;
    left: 0;
    right: 0;
    text-align: center;
    font-weight: 400;
    font-size: 19px;
  }
</style>
</head>
<body>
  <main class="label">
    <div class="label-frame"></div>

    <header class="brand">
      <span class="brand-mark"></span>
      <div class="brand-name">VELTRIX</div>
      <div class="brand-tagline">PROFESSIONAL</div>
    </header>

    <h1 class="product-name">PET<br>SHAMPOO</h1>

    <div class="pet-icon" role="img" aria-label="Simple white line icon of a dog's head"></div>

    <section class="claim">
      <p class="claim-title">DAILY HAIR CLEANSE</p>
      <p class="claim-note">FOR PETS ONLY</p>
    </section>

    <p class="net-weight">Nt weight )z16</p>
  </main>
</body>
</html>
```